Label Design VelmoRest Capsules

Hello dear designers!

We run a brand for dietary supplements and are looking for a talented designer to help take our brand to the next level. We are planning to launch new products with fresh packaging and redesigned labels. Additionally, we would like to refresh our company logo to make it fit better on the packaging.

Important Info:

Our brand: VelmoPure – specializing in products for detoxification, sleep, and eye protection.
Our shop: www.velmopure.at – currently offering two main products:
VelmoPure (Detox Tincture)
Velmo Optic Guard (Blue Light Filter Glasses)
Project Goal: Initially, we are looking for a label design for our new product VelmoRest (sleep capsules). If we like the design, we would like to revise the label for our first product, VelmoPure, and potentially rework our logo to make it more compact and visually appealing on our packaging.

Design Preferences: We are fans of the design style of Farv Nutra and would love a design in a similar style – modern, clean, and premium – but with a unique touch that fits our brand. You will find some inspirations and ideas that we particularly like in the attachment.

Important:

Our packaging for VelmoRest is an 8 OZ jar (similar to the smaller jars used by Farv Nutra).
The label should be clear, appealing, and give the product a high-quality look.
An example of a previous design draft (which hasn’t fully convinced us yet), along with inspirations for our upcoming bundle (including VelmoPure, VelmoRest, and VelmoOptic Guard), is also attached.
Special Opportunity: The designer with the best concept will have the chance to collaborate with us long-term! We have two more brands in the pipeline and are looking for a reliable and creative partner for future projects. Generous compensation and tips are guaranteed.

We look forward to seeing creative and professional designs that will take our brand to the next level!

Target Market(s)

Germany

Industry/Entity Type

Supplement

Font styles to use
Sans Serif

Colors

Designer to choose colors to be used in the design.

Requirements
Must have
• Es sollte Hochwertig und Modern aussehen. Matt schwarzer hintergrund. less is more
Nice to have
• Maybe The head should be visible in the background.
Should not have
• it should not be colorful, and not too playful, it should definitely not look cheap!

```html
<!DOCTYPE html>
<html lang="de">
<head>
<meta charset="utf-8">
<title>Velmo Rest – Etikett</title>
<link rel="stylesheet" href="https://fonts.googleapis.com/css2?family=Bebas+Neue&family=Barlow+Condensed:ital,wght@0,500;0,600;1,700&family=Barlow+Semi+Condensed:wght@400;600&display=swap">
<style>
  :root {
    --page: #ffffff;
    --label: #1b1b1d;
    --label-deep: #0d0d0e;
    --text: #ececec;
    --muted: #cfcfcf;
    --accent: #1fc6ef;
    --gold: #c9a86a;
    --frame: #3a3a3d;
  }
  * { margin: 0; padding: 0; box-sizing: border-box; }
  html, body { width: 1200px; height: 528px; overflow: hidden; background: var(--page); }
  .canvas { position: relative; width: 1200px; height: 528px; }
  .label {
    position: absolute; left: 40px; top: 41px; width: 1120px; height: 447px;
    background: var(--label); color: var(--text); overflow: hidden;
    font-family: "Barlow Semi Condensed", "Arial Narrow", sans-serif;
  }
  .head-art {
    position: absolute; left: 380px; top: 0; width: 400px; height: 447px;
    background:
      radial-gradient(ellipse 120px 110px at 200px 40px, #0a0a0b 0%, #0a0a0b 60%, transparent 62%),
      radial-gradient(ellipse 180px 220px at 200px 200px, rgba(255,255,255,0.07), transparent 70%),
      linear-gradient(180deg, #19191b, #1d1d1f);
  }
  .base-band {
    position: absolute; left: 420px; top: 411px; width: 282px; height: 36px;
    background: var(--label-deep); border-radius: 14px 14px 0 0;
  }

  /* left column */
  .info { position: absolute; left: 18px; top: 25px; width: 323px; font-size: 9.6px; line-height: 13px; }
  .info p { text-align: justify; }
  .info strong { font-weight: 600; }
  .section-title {
    font-family: "Barlow Condensed", sans-serif; font-weight: 600; color: var(--accent);
    font-size: 14px; letter-spacing: 0.2px; margin: 11px 0 11px;
  }
  .gap { margin-top: 12px; }
  .contact-box {
    position: absolute; left: 18px; top: 223px; width: 323px; height: 76px;
    border: 1px solid var(--frame); border-radius: 5px; text-align: center;
    font-size: 12px; line-height: 15.6px; padding-top: 5px;
  }
  .contact-box .brand {
    font-family: "Barlow Condensed", sans-serif; font-weight: 600; color: var(--accent); font-size: 12.5px;
  }
  .storage { position: absolute; left: 18px; top: 311px; width: 323px; text-align: center; font-size: 10px; line-height: 13.6px; font-weight: 600; }

  /* centre */
  .brandmark {
    position: absolute; left: 440px; width: 320px; top: 38px; text-align: center;
    font-family: "Barlow Condensed", sans-serif; font-weight: 500; color: var(--gold);
    font-size: 12px; letter-spacing: 2.6px;
  }
  .brandmark .dot { display: block; width: 14px; height: 14px; margin: 8px auto 0; border-radius: 50%; border: 1.2px solid var(--gold); }
  .product-name {
    position: absolute; left: 400px; width: 400px; top: 142px; text-align: center;
    font-family: "Bebas Neue", sans-serif; font-size: 86px; line-height: 86px; color: #fff; letter-spacing: 0.5px;
  }
  .claim {
    position: absolute; left: 401px; top: 228px; width: 318px; height: 42px;
    border: 2px solid var(--accent); border-radius: 21px; text-align: center;
    font-family: "Barlow Condensed", sans-serif; font-style: italic; font-weight: 700;
    color: var(--accent); font-size: 27px; line-height: 38px; letter-spacing: 0.3px;
  }
  .benefits { position: absolute; left: 455px; top: 300px; list-style: none; }
  .benefits li {
    font-family: "Bebas Neue", sans-serif; font-size: 18.5px; line-height: 26px; color: #fff; letter-spacing: 0.3px;
    display: flex; align-items: center;
  }
  .benefits li::before { content: ""; width: 2.5px; height: 12px; background: var(--accent); margin-right: 8px; }
  .pack-size {
    position: absolute; left: 420px; width: 282px; top: 418px; text-align: center;
    font-family: "Bebas Neue", sans-serif; font-size: 19px; color: #fff; letter-spacing: 0.5px;
  }
  .pack-size .sep { color: var(--accent); margin: 0 3px; }

  /* right column */
  .facts { position: absolute; left: 779px; top: 26px; width: 322px; font-size: 9.6px; line-height: 12.9px; }
  .facts p { text-align: justify; }
  .facts .section-title { font-size: 16px; margin: 0 0 8px; font-family: "Barlow Condensed", sans-serif; }
  .facts strong { font-weight: 600; }
  .facts .block { margin-top: 10px; }
  .facts .note { margin-top: 12px; }
</style>
</head>
<body>
<div class="canvas">
  <div class="label">
    <div class="head-art" role="img" aria-label="Faint silhouette of a human head with circuit lines, dark grey on black"></div>
    <div class="base-band"></div>

    <section class="info">
      <p><strong>Velmo Rest</strong> ist ein Nahrungsergänzungsmittel von der Firma VelmoPure auf Basis von Kräuterextrakten, Vitaminen und Mineralstoffen in Kapselform. Ohne Zusatz von Konservierungs- und Farbstoffen.</p>
      <h2 class="section-title">VERZEHREMPFEHLUNG:</h2>
      <p>Am besten abends 2 Kapseln vor dem Schlafen gehen zusammen mit Wasser einnehmen. Die empfohlene tägliche Verzehrmenge nicht überschreiten.</p>
      <p class="gap">Außerhalb der Reichweite von Kindern aufbewahren. Nahrungsergänzungsmittel sind kein Ersatz für eine abwechslungsreiche Ernährung. Eine abwechslungsreiche und ausgewogene Ernährung und gesunde Lebensweise sind wichtig.</p>
      <p class="gap" style="margin-top:16px">Für mehr Informationen und weitere Produkte:</p>
    </section>

    <div class="contact-box">
      <div class="brand">VELMOPURE</div>
      <div>Lukas Brenner, Lindenweg 14, 6900 Bregenz</div>
      <div>Hersteller: Verdana Botanics – Kestrel Ind. Pvt. Ltd. 212/7</div>
      <div>Harwal Estate Surat, 395010 Gujarat</div>
    </div>

    <div class="storage">
      <div>Mindestens haltbar bis: siehe Bodenetikett</div>
      <div>Vor Wärme und Sonneneinstrahlung geschütz lagern!</div>
    </div>

    <div class="brandmark">VELMOPURE<span class="dot"></span></div>
    <h1 class="product-name">VELMO REST</h1>
    <div class="claim">FÖRDERT DIE TIEFSCHLAFPHASE</div>
    <ul class="benefits">
      <li>ZWISCHENÜBERSCHRIFT HINZUFÜGEN</li>
      <li>ZWISCHENÜBERSCHRIFT HINZUFÜGEN</li>
      <li>ZWISCHENÜBERSCHRIFT HINZUFÜGEN</li>
    </ul>
    <div class="pack-size">30 PORTIONEN<span class="sep">|</span>60 KAPSELN</div>

    <section class="facts">
      <h2 class="section-title">ZUTATEN</h2>
      <p>Magnesium, Kamillenblüte, Lindenblüte, Melissenkraut, Avena sativa Kraut, Pfefferminze Kraut, Passionsblumenkraut, Echte Katzenminze Kraut, Ingwer, Echtes Steinkleekraut, Süsser Majoran, Echtes Mädesüß Blüte, Weideröschenkraut, Baldrian, Lavendelblüte, Süßholzwurzel, Schisandrafrucht, Myristica Fragrans Samenmantel, Rosa Centifolia-Rosenblüten, Thymian, Hopfenblüte Niacin (Vitamin B3), Ehrenpreiskraut, Klatschmohnblüte, Pantothensäure, Zink, Vitamin B6, Vitamin B2, Vitamin B1, Folsäure, Selen, Biotin, B12.</p>
      <p class="block"><strong>2 Kapseln (empfohlene tägl. Verzehrmenge enthält Konzentrate aus:)</strong><br>Kamillenblüte 590 mg, 1:5; Lindenblüte 590 mg, 1:5; Melissenkraut 290 mg, 1:5; Avena sativa Kraut 290 mg, 1:5; Pefferminze Kraut 290 mg, 1:5; Passionsblumenkraut 140 mg, 1:5; Echte Katzenminze Kraut 280 mg, 1:10; Ingwer 190 mg, 1:10; Echtes Steinkleekraut 190 mg, 1:10, Süsser Majoran 190 mg, 1:10; Echtes Mädesüß Blüte 190 mg, 1:10, Weideröschenkraut 190 mg, 1:10; Baldrian 90 mg, 1:5; Lavendelblüte 70 mg, 1:5; Süßholzwurzel 140 mg, 1:10; Schisandrafrucht 140 mg, 1:10; Myristica Fragrans Samenmantel 90 mg, 1:10; Rosa Centifolia-Rosenblüten 90 mg, 1:10; Thymian 90 mg, 1:10; Hopfenblüte 40 mg, 1:5; Ehrenpreiskraut 70 mg, 1:10; Klatschmohnblüte 70 mg, 1:10;</p>
      <p class="block"><strong>und enthalten:</strong> Magnesium (Magnesiumchlorid) 370 mg (98% NRV*); Niacin (aktivierte Nikotinsäure) 8 mg (50% NRV*); Pantothensäure (Pantethin) 6 mg (100% NRV*); Zink (Zink Bisglycinat) 3.2 mg (32% NRV*) Vitamin B6 (Pyridoxin) 2.8 mg (200% NRV*); Vitamin B2 (Riboflavin-5-phosphat) 1.6 mg (114% NRV*); Vitamin B1 (Thiaminhydrochlorid) 1.65 mg (145% NRV*); Folsäure (Calcium-L-methylfolat) 200 µg (100% NRV*); Selen (L-Selenomethionin) 80 µg (145% NRV*); D-Biotin 40 µg (80% NRV*); B12 (5-deoxyadenosylcobalamin) 6.8 µg (272% NRV*)</p>
      <p class="note">*NRV: Prozent d.er Nährstoffbezugswerte gemäß LebensmittelinformationsVO</p>
    </section>
  </div>
</div>
</body>
</html>
```